Accountancy firm needs clean and simple website and optional logo

We need a logo and basic wordpress website design for a Sydney based accountancy firm.
We need a clean and simple logo and website, based on the accounting/finance/tax industry. Simple, credible and official colors.
The logo is expected to be so simple that we have combined into the one job.
If you submit a logo design and we choose it along with someone else's website design you will be paid a bonus of $60. The website design will still win the competition as per normal.
Current website is old and terrible but gives you an idea of the sitemap (super simple) and what they do: www.brookfiscal.com.au
We want original different to normal template looking designs.
We like videos, and like http://www.whitfords.com.au/
Feel free to go to vidhaven and use some videos from there.
We are based in Sydney Australia and in the field of taxation and accounting
We want a clean, formal, credible site, limited pages.
The project is guaranteed, so go for it.
Brook & Associates
1 page

```html
<!DOCTYPE html>
<html lang="en">
<head>
<meta charset="utf-8">
<title>Brook &amp; Associates</title>
<link href="https://fonts.googleapis.com/css2?family=Open+Sans:wght@400;600;700&family=Playfair+Display:wght@700&display=swap" rel="stylesheet">
<style>
:root{
  --blue:#1e88d8;
  --blue-dark:#1667ad;
  --ink:#2d2d2d;
  --muted:#8a8f96;
  --line:#e4e6ea;
  --hero:#3b4756;
  --footer:#2a2c2f;
  --footer-deep:#1f2123;
  --white:#ffffff;
}
*{box-sizing:border-box;margin:0;padding:0}
html,body{width:686px;height:1200px;overflow:hidden}
body{font-family:"Open Sans",Arial,sans-serif;color:var(--ink);background:var(--white);font-size:8px;line-height:1.5}
ul{list-style:none}

.site-header{height:69px;display:flex;align-items:center;padding:0 40px}
.brand{display:flex;align-items:center;gap:8px;width:265px}
.brand-mark{width:26px;height:26px;background:var(--blue)}
.brand-name{font-weight:700;font-size:11px;color:var(--blue-dark)}
.header-info{display:flex;align-items:center;gap:6px;font-size:9px;color:var(--blue-dark);font-weight:600}
.header-info small{display:block;font-weight:400;color:var(--muted);font-size:7px}
.header-info + .header-info{margin-left:48px}

.main-nav{height:23px;background:var(--blue);display:flex;align-items:center;padding:0 40px}
.main-nav a{color:var(--white);text-decoration:none;font-size:8px;width:80px;height:23px;line-height:23px;text-align:center}
.main-nav a.active{background:var(--blue-dark)}
.nav-social{margin-left:auto;display:flex;gap:6px}
.nav-social span{width:13px;height:13px;border-radius:50%;background:rgba(255,255,255,.35)}

.hero{position:relative;height:293px;background:linear-gradient(180deg,#4a5666,#2f3a48)}
.hero-photo{position:absolute;inset:0;background:linear-gradient(120deg,#56616f 0%,#3a4452 55%,#2c3643 100%);opacity:.9}
.hero-content{position:absolute;left:0;right:0;top:118px;text-align:center;color:var(--white)}
.hero h1{font-family:"Playfair Display",Georgia,serif;font-size:18px;letter-spacing:1px;line-height:1.35;text-transform:uppercase}
.hero p{font-size:6.5px;width:420px;margin:10px auto 0;color:#dde3ea}
.btn{display:inline-block;background:var(--blue);color:var(--white);font-size:7px;font-weight:600;padding:6px 16px;text-transform:uppercase}
.hero .btn{margin-top:18px}
.hero-arrow{position:absolute;top:140px}
.hero-arrow.left{left:8px}.hero-arrow.right{right:8px}

.section-title{font-family:"Playfair Display",Georgia,serif;font-size:20px;text-align:center;color:var(--ink)}
.section-title span,.col-title span{color:var(--blue)}
.section-sub{text-align:center;color:var(--muted);font-size:6px;margin-top:4px}
.services{padding-top:27px}
.services .section-title{position:relative}
.services .section-title::after{content:"";display:block;width:40px;height:2px;background:var(--blue);margin:3px auto 0}
.cards{display:flex;justify-content:center;gap:18px;margin-top:20px}
.card{width:172px;height:183px;background:var(--white);box-shadow:0 1px 5px rgba(0,0,0,.14)}
.card-media{height:80px}
.card-body{padding:8px 10px}
.card-body h3{font-size:8.5px;font-weight:600;margin-bottom:4px}
.card-body li{font-size:6.5px;color:var(--muted);line-height:1.7}

.features{display:flex;justify-content:center;gap:40px;margin-top:28px}
.feature-col{width:240px}
.col-title{font-family:"Playfair Display",Georgia,serif;font-size:13px;margin-bottom:14px}
.feature{display:flex;gap:10px;margin-bottom:16px;height:56px}
.feature-icon{width:22px;flex:none}
.feature-thumb{width:50px;height:32px;flex:none}
.feature h4{font-size:6.5px;font-weight:700;text-transform:uppercase;margin-bottom:3px}
.feature p{font-size:6px;color:var(--muted);line-height:1.6}
.feature-col .btn{margin-top:6px}

.partners{display:flex;align-items:center;justify-content:center;gap:32px;margin-top:30px;height:60px}
.partner{width:44px;height:44px;border-radius:50%;border:2px solid #b9bdc3}
.partner.square{border-radius:4px}

.site-footer{position:absolute;top:1019px;left:0;width:686px;height:181px;background:var(--footer);color:#c9ccd0}
.footer-cols{display:flex;padding:22px 40px 0;gap:22px}
.footer-col{width:135px}
.footer-col h5{color:var(--white);font-size:10px;font-weight:600;margin-bottom:10px}
.quick-links li{font-size:7px;line-height:1.9}
.quick-links li::before{content:"› ";color:var(--blue)}
.news-item{display:flex;gap:6px;margin-bottom:8px}
.news-thumb{width:22px;height:22px;background:#5b6572;flex:none}
.news-item b{display:block;font-size:7px;color:var(--white);font-weight:600}
.news-item span{font-size:6px}
.contact-row{display:flex;gap:6px;font-size:6.5px;margin-bottom:6px}
.about-text{font-size:6.5px;line-height:1.6}
.footer-social{display:flex;gap:5px;margin-top:8px}
.footer-social span{width:13px;height:13px;border-radius:50%;background:#555a60}
.footer-bottom{position:absolute;bottom:0;left:0;right:0;height:20px;background:var(--footer-deep);text-align:center;font-size:6.5px;line-height:20px;color:#9ba0a6}
</style>
</head>
<body>

<header class="site-header">
  <div class="brand">
    <div class="brand-mark"></div>
    <div class="brand-name">Brook &amp; Associates</div>
  </div>
  <div class="header-info">
    <svg width="12" height="12" viewBox="0 0 24 24"><path fill="#1e88d8" d="M6.6 10.8a15 15 0 006.6 6.6l2.2-2.2a1 1 0 011-.25 11.4 11.4 0 003.6.57 1 1 0 011 1V20a1 1 0 01-1 1A17 17 0 013 4a1 1 0 011-1h3.5a1 1 0 011 1c0 1.25.2 2.45.57 3.57a1 1 0 01-.25 1z"/></svg>
    <div>07 4512 9087<small>www.brookfiscal.com.au</small></div>
  </div>
  <div class="header-info">
    <svg width="12" height="12" viewBox="0 0 24 24"><path fill="#1e88d8" d="M12 2a7 7 0 00-7 7c0 5.25 7 13 7 13s7-7.75 7-13a7 7 0 00-7-7zm0 9.5A2.5 2.5 0 1112 6.5a2.5 2.5 0 010 5z"/></svg>
    <div>Physical 4/12 Harbour Lane<small>Sydney NSW 2000</small></div>
  </div>
</header>

<nav class="main-nav">
  <a class="active">Home</a><a>Accounts</a><a>About Us</a><a>News</a><a>Contact Us</a>
  <div class="nav-social"><span></span><span></span><span></span><span></span></div>
</nav>

<section class="hero">
  <div class="hero-photo" role="img" aria-label="Hands working at a laptop and calculator on a desk, darkened"></div>
  <svg class="hero-arrow left" width="10" height="14" viewBox="0 0 10 14"><path d="M8 1L2 7l6 6" stroke="#fff" stroke-width="2" fill="none"/></svg>
  <svg class="hero-arrow right" width="10" height="14" viewBox="0 0 10 14"><path d="M2 1l6 6-6 6" stroke="#fff" stroke-width="2" fill="none"/></svg>
  <div class="hero-content">
    <h1>Take the worry out of tax<br>and the business</h1>
    <p>We look after your returns, bookkeeping and planning so you can spend more time running your business with total confidence and clear numbers every year.</p>
    <a class="btn">Read More</a>
  </div>
</section>

<section class="services">
  <h2 class="section-title">Our <span>Services</span></h2>
  <p class="section-sub">Practical tax and accounting help for local families and growing businesses</p>
  <div class="cards">
    <article class="card">
      <div class="card-media" role="img" aria-label="Calculator, glasses and papers on a desk" style="background:linear-gradient(135deg,#7d9fc0,#c7b48a)"></div>
      <div class="card-body"><h3>Taxes and Accounts</h3>
        <ul><li>Tax planning and returns</li><li>Residential loans and financing</li><li>Superannuation self managed funds</li><li>Estate planning support</li></ul></div>
    </article>
    <article class="card">
      <div class="card-media" role="img" aria-label="Person typing on a laptop" style="background:linear-gradient(135deg,#a9c3dd,#4f77a6)"></div>
      <div class="card-body"><h3>Neque Porro Quisquam</h3>
        <ul><li>GST preparation and lodgement</li><li>Not for profit companies and trusts</li><li>Business setup</li><li>Accounting system establishment</li></ul></div>
    </article>
    <article class="card">
      <div class="card-media" role="img" aria-label="Businessman in a suit at an office" style="background:linear-gradient(135deg,#d6dde5,#56606c)"></div>
      <div class="card-body"><h3>Tempora Incidunt Labore</h3>
        <ul><li>Litigation assistance</li><li>Business advisory services</li><li>Growth protection services</li><li>Business planning</li></ul></div>
    </article>
  </div>
</section>

<section class="features">
  <div class="feature-col">
    <h3 class="col-title">Our <span>Advantages</span></h3>
    <div class="feature">
      <svg class="feature-icon" viewBox="0 0 24 24" height="22"><circle cx="12" cy="12" r="10" fill="none" stroke="#555" stroke-width="1.6"/><ellipse cx="12" cy="12" rx="4.5" ry="10" fill="none" stroke="#555" stroke-width="1.4"/><path d="M2 12h20" stroke="#555" stroke-width="1.4"/></svg>
      <div><h4>Local advice from trusted advisers</h4><p>Our team knows the Sydney market and works closely with each client to keep their affairs in order, lodged on time and fully compliant.</p></div>
    </div>
    <div class="feature">
      <svg class="feature-icon" viewBox="0 0 24 24" height="22"><rect x="2" y="4" width="16" height="17" fill="none" stroke="#555" stroke-width="1.6"/><path d="M10 14l1-4 9-8 3 3-9 8z" fill="#555"/></svg>
      <div><h4>Clear fees and honest reporting</h4><p>You always know what you pay and why. We explain each report in plain words so you can make sound decisions for the year ahead.</p></div>
    </div>
    <a class="btn">Read More</a>
  </div>
  <div class="feature-col">
    <h3 class="col-title">Our <span>Capabilities</span></h3>
    <div class="feature">
      <div class="feature-thumb" role="img" aria-label="Pen and financial chart" style="background:linear-gradient(135deg,#cfd6de,#8a97a6)"></div>
      <div><h4>Business growth planning</h4><p>We build forecasts, budgets and cash flow plans that help owners grow steadily and prepare for change in any season.</p></div>
    </div>
    <div class="feature">
      <div class="feature-thumb" role="img" aria-label="Desk with documents and laptop" style="background:linear-gradient(135deg,#6b7785,#2f3844)"></div>
      <div><h4>Complete tax compliance</h4><p>From simple returns to complex trust structures, we handle lodgements and reviews with care and full attention to detail.</p></div>
    </div>
    <a class="btn">Read More</a>
  </div>
</section>

<section class="partners">
  <svg width="8" height="12" viewBox="0 0 8 12"><path d="M6 1L1 6l5 5" stroke="#999" stroke-width="1.5" fill="none"/></svg>
  <div class="partner"></div><div class="partner square"></div><div class="partner"></div><div class="partner"></div><div class="partner"></div><div class="partner square"></div>
  <svg width="8" height="12" viewBox="0 0 8 12"><path d="M2 1l5 5-5 5" stroke="#999" stroke-width="1.5" fill="none"/></svg>
</section>

<footer class="site-footer">
  <div class="footer-cols">
    <div class="footer-col">
      <h5>Quick Links</h5>
      <ul class="quick-links"><li>Features</li><li>Services</li><li>Our Blog</li><li>About</li><li>Contact</li></ul>
    </div>
    <div class="footer-col">
      <h5>Latest News</h5>
      <div class="news-item"><div class="news-thumb" role="img" aria-label="News thumbnail"></div><div><b>Ruth Mallory</b><span>Key changes to this year's tax rules</span></div></div>
      <div class="news-item"><div class="news-thumb" role="img" aria-label="News thumbnail"></div><div><b>Owen Tasker</b><span>Preparing your books for year end</span></div></div>
    </div>
    <div class="footer-col">
      <h5>Contact</h5>
      <div class="contact-row"><svg width="8" height="8" viewBox="0 0 24 24"><path fill="#1e88d8" d="M12 2a7 7 0 00-7 7c0 5.25 7 13 7 13s7-7.75 7-13a7 7 0 00-7-7z"/></svg><span>Office 3, 48 Kent Street<br>Sydney NSW 2000</span></div>
      <div class="contact-row"><svg width="8" height="8" viewBox="0 0 24 24"><path fill="#1e88d8" d="M6.6 10.8a15 15 0 006.6 6.6l2.2-2.2a1 1 0 011-.25 11.4 11.4 0 003.6.57 1 1 0 011 1V20a1 1 0 01-1 1A17 17 0 013 4a1 1 0 011-1h3.5a1 1 0 011 1c0 1.25.2 2.45.57 3.57a1 1 0 01-.25 1z"/></svg><span>+61 2 9188 4402</span></div>
    </div>
    <div class="footer-col">
      <h5>About Us</h5>
      <p class="about-text">A small Sydney practice offering friendly tax, accounting and advisory services to individuals and businesses across the city.</p>
      <div class="footer-social"><span></span><span></span><span></span><span></span><span></span></div>
    </div>
  </div>
  <div class="footer-bottom">© 2016 Brook &amp; Associates. All Rights Reserved</div>
</footer>

</body>
</html>
```